Tradeshow display - back drop and matching podium wrap

Looking for a design for a tradeshow display 136.22" x 90.55". and there is approximately 12.25" side panels on each side here (see attached). Needs design for matching podium wrap as well (specs attached).
You can take a look at our website to get a feel on who we are.
www.brindlecrestflow.com
I've added a design I like so you get an idea of what I'm wanting here.
We do not want the Lumora logos on the banner please.
We do water treatment using ozone.

Industry/Entity Type

Agriculture

Requirements
Should not have
• the lumora logos

```html
<!DOCTYPE html>
<html lang="en">
<head>
<meta charset="utf-8">
<title>Brindlecrest Flow – Tradeshow Backdrop and Podium Wrap</title>
<link href="https://fonts.googleapis.com/css2?family=Oswald:wght@500;700&family=Open+Sans:wght@600&display=swap" rel="stylesheet">
<style>
  :root {
    --stage: #c9c9c9;
    --white: #ffffff;
    --mist: #e9eaec;
    --brand-blue: #1a6bb8;
    --deep-blue: #0d3f8f;
    --navy: #0a2e78;
    --ink: #1f2a3a;
  }
  * { box-sizing: border-box; margin: 0; padding: 0; }
  html, body { width: 1200px; height: 840px; overflow: hidden; }
  body {
    background: var(--stage);
    font-family: "Oswald", "Arial Narrow", sans-serif;
    position: relative;
  }

  /* Podium wrap */
  .podium-wrap {
    position: absolute;
    left: 40px; top: 330px;
    width: 230px; height: 360px;
    background: linear-gradient(90deg, var(--mist), var(--white) 40%, var(--white) 70%, var(--mist));
    display: flex; align-items: center; justify-content: center;
  }
  .podium-wrap .brand-name {
    font-weight: 700; font-size: 44px; line-height: 0.95;
    color: var(--deep-blue); text-align: center;
  }

  /* Backdrop */
  .backdrop {
    position: absolute;
    left: 300px; top: 120px;
    width: 860px; height: 600px;
    background: linear-gradient(90deg, var(--white) 0%, var(--mist) 30%, var(--white) 75%);
    overflow: hidden;
  }
  .backdrop .band { position: absolute; inset: 0; }
  .backdrop .brand-name {
    position: absolute; top: 62px; left: 0; right: 0;
    text-align: center; font-weight: 700; font-size: 66px; line-height: 1;
    color: var(--brand-blue);
  }
  .tagline {
    position: absolute; top: 180px; left: 0; right: 0;
    display: flex; justify-content: center; align-items: center; gap: 6px;
  }
  .tagline-box {
    border: 2px solid var(--brand-blue);
    padding: 3px 18px;
    font-weight: 500; font-size: 19px; color: var(--brand-blue);
    letter-spacing: .3px; background: var(--white); border-radius: 4px;
  }
  .tagline-equals {
    font-weight: 700; font-size: 18px; color: var(--white);
    background: var(--brand-blue); padding: 0 8px; line-height: 24px;
  }
  .url-pill {
    position: absolute; top: 228px; left: 50%; transform: translateX(-50%);
    background: var(--brand-blue); color: var(--white);
    font-weight: 500; font-size: 20px; letter-spacing: .5px;
    padding: 2px 22px; border-radius: 5px; white-space: nowrap;
  }
  .side-url {
    position: absolute; top: 440px;
    font-family: "Open Sans", Arial, sans-serif; font-weight: 600;
    font-size: 12px; letter-spacing: 1.5px; color: var(--white);
    white-space: nowrap;
  }
  .side-url--left { left: 32px; transform: translate(-50%, -50%) rotate(90deg); }
  .side-url--right { left: 830px; transform: translate(-50%, -50%) rotate(-90deg); }

  .service-cards {
    position: absolute; top: 345px; left: 0; right: 0;
    display: flex; justify-content: center; gap: 18px;
  }
  .service-card {
    width: 152px; height: 228px;
    background: linear-gradient(180deg, var(--white), var(--mist));
    clip-path: polygon(12px 0, calc(100% - 12px) 0, 100% 12px, 100% calc(100% - 12px), calc(100% - 12px) 100%, 12px 100%, 0 calc(100% - 12px), 0 12px);
    display: flex; flex-direction: column; align-items: center; justify-content: center;
    padding: 0 12px; text-align: center;
  }
  .service-title {
    font-weight: 500; font-size: 16px; line-height: 1.15; color: var(--ink);
  }
  .service-text {
    margin-top: 12px; font-family: "Open Sans", Arial, sans-serif; font-weight: 600;
    font-size: 10px; line-height: 1.45; color: var(--ink);
  }
</style>
</head>
<body>

  <section class="podium-wrap" aria-label="Podium wrap">
    <div class="brand-name">brindlecrest<br>flow</div>
  </section>

  <section class="backdrop" aria-label="Backdrop">
    <svg class="band" width="860" height="600" viewBox="0 0 860 600" aria-hidden="true">
      <defs>
        <linearGradient id="bandFill" x1="0" y1="0" x2="1" y2="0">
          <stop offset="0" stop-color="#0a2e78"/>
          <stop offset="0.2" stop-color="#1e6fc0"/>
          <stop offset="0.8" stop-color="#1e6fc0"/>
          <stop offset="1" stop-color="#1a5fae"/>
        </linearGradient>
      </defs>
      <polygon points="0,250 430,300 860,248 860,600 0,600" fill="url(#bandFill)"/>
      <polyline points="0,262 430,312 860,260" fill="none" stroke="#ffffff" stroke-width="3"/>
    </svg>

    <div class="brand-name">brindlecrest flow</div>

    <div class="tagline">
      <span class="tagline-box">HIGH-QUALITY FARM WATER</span>
      <span class="tagline-equals">=</span>
      <span class="tagline-box">HEALTHY HIGH-PERFORMANCE FARMS</span>
    </div>

    <div class="url-pill">WWW.BRINDLECRESTFLOW.COM</div>

    <div class="side-url side-url--left">WWW.BRINDLECRESTFLOW.COM</div>
    <div class="side-url side-url--right">WWW.BRINDLECRESTFLOW.COM</div>

    <div class="service-cards">
      <article class="service-card">
        <h3 class="service-title">DAIRY WATER TREATMENT</h3>
        <p class="service-text">Over the years our dairy systems have treated billions of gallons of water.</p>
      </article>
      <article class="service-card">
        <h3 class="service-title">POULTRY WATER TREATMENT</h3>
        <p class="service-text">Take a look at our new Bio-Security system for poultry operations.</p>
      </article>
      <article class="service-card">
        <h3 class="service-title">SWINE WATER TREATMENT</h3>
        <p class="service-text">Quality water intake for swine operations is critical to both health and growth.</p>
      </article>
      <article class="service-card">
        <h3 class="service-title">GREENHOUSE DISINFECTION</h3>
        <p class="service-text">Enhance both Greenhouse sanitation and plant performance.</p>
      </article>
    </div>
  </section>

</body>
</html>
```